"Aviation Law Firm Needs Banner for Fly-In Website"

My firm is looking for a web banner which will be advertised on www.kestrel-meet.org. The banner is going to be used for advertisement leading up to the big fly-in event being held in April.

My law firm represents pilots, plane owners, airlines, and anyone else that has an interest in aviation.

I would like to see some animation if possible, which would include aviation/cutting edge themes.

I would like to incorporate my logo and background images from my website (attached).

The advertisement should discretely near the firm name say "Offices: Brookvale"

The advertised words should be "Vectoring You Through Legal Turbulence"

The advertisement should also include my telephone number: "1-855-ROW-4738" and also my website "www.TheCounselDesk.com"

The call to action should say "Contact The Counsel Desk"

This is a Vertical Ad and its dimensions are 300x600 PX (72 DPI)

Must be in PNG or JPEG format.

Target Market(s)

Pilots/Aviation Enthusiasts

Industry/Entity Type

Law Firm

Font styles to use
Serif
Sans Serif

Colors
fbf289
fbed22
ffffff
1b1b1b
000000

Requirements
Must have
• The banner should definitely look professional, yet cutting edge. The banner definitely needs those things listed in the project description.
Nice to have
• Animation

```html
<!DOCTYPE html>
<html lang="en">
<head>
<meta charset="utf-8">
<title>The Marlow Law Firm – Vertical Banner Variants</title>
<link href="https://fonts.googleapis.com/css2?family=Bebas+Neue&family=Cinzel:wght@400&family=Oswald:wght@500&family=Playfair+Display:ital,wght@1,400;1,700&family=Michroma&display=swap" rel="stylesheet">
<style>
  :root{
    --yellow:#fbed22;
    --pale-yellow:#fbf289;
    --white:#ffffff;
    --charcoal:#1b1b1b;
    --black:#000000;
    --ghost:#1e1e1e;
    --ghost-icon:#2b2b2b;
    --rule:#2a2a2a;
  }
  html,body{margin:0;padding:0;width:1200px;height:899px;overflow:hidden;background:var(--white);}
  .sheet{position:relative;width:1200px;height:899px;}
  .banner{position:absolute;top:138px;width:300px;height:600px;background:var(--black);overflow:hidden;}
  .banner--muted{left:248px;}
  .banner--lit{left:618px;}

  .runway-photo{
    position:absolute;left:0;top:477px;width:300px;height:123px;
    background:
      radial-gradient(ellipse 55px 50px at 125px 70px,#d8d48a 0%,#8c8a3e 45%,transparent 78%),
      linear-gradient(180deg,#000 0%,#1a1a08 25%,#55531f 65%,#b4b05a 100%);
  }
  .artwork{position:absolute;left:0;top:0;width:300px;height:600px;}

  .brand-dot{fill:var(--pale-yellow);}
  .brand-name{font-family:"Cinzel",serif;font-size:15px;fill:var(--white);}
  .practice{font-family:"Cinzel",serif;font-size:7.5px;fill:var(--white);}
  .practice-rule{stroke:var(--white);stroke-width:1;}
  .tagline-band{fill:var(--yellow);}
  .tagline{font-family:"Playfair Display",serif;font-style:italic;font-weight:700;font-size:26px;fill:var(--charcoal);}
  .office{font-family:"Playfair Display",serif;font-style:italic;font-size:17px;fill:var(--pale-yellow);}
  .cta{font-family:"Bebas Neue",sans-serif;}
  .banner--muted .cta{fill:var(--ghost);}
  .banner--lit .cta{fill:var(--yellow);}
  .bulb--off{fill:var(--ghost-icon);}
  .bulb--on{fill:var(--yellow);}
  .bulb-rays{stroke:var(--yellow);stroke-width:2.2;stroke-linecap:round;}
  .divider{fill:var(--rule);}
  .phone{font-family:"Michroma",sans-serif;font-size:21px;fill:var(--pale-yellow);stroke:var(--pale-yellow);stroke-width:.7;}
  .web{font-family:"Oswald",sans-serif;font-weight:500;font-size:21px;fill:var(--pale-yellow);}
</style>
</head>
<body>
<main class="sheet">

  <article class="banner banner--muted">
    <div class="runway-photo" role="img" aria-label="Yellow-tinted photo of a jet airliner nose-on at a night runway"></div>
    <svg class="artwork" viewBox="0 0 300 600">
      <circle class="brand-dot" cx="42" cy="32" r="17"/>
      <text class="brand-name" x="177" y="32" text-anchor="middle" textLength="152" lengthAdjust="spacingAndGlyphs">The Marlow Law Firm</text>
      <line class="practice-rule" x1="88" y1="43" x2="116" y2="43"/>
      <text class="practice" x="186" y="46" text-anchor="middle" textLength="136" lengthAdjust="spacingAndGlyphs">AVIATION LAW | DRONE LAW</text>
      <line class="practice-rule" x1="257" y1="43" x2="272" y2="43"/>
      <rect class="tagline-band" x="0" y="73" width="300" height="68"/>
      <text class="tagline" x="152" y="105" text-anchor="middle" textLength="146" lengthAdjust="spacingAndGlyphs">VECTORING YOU</text>
      <text class="tagline" x="152" y="129" text-anchor="middle" textLength="272" lengthAdjust="spacingAndGlyphs">THROUGH LEGAL TURBULENCE</text>
      <text class="office" x="150" y="168" text-anchor="middle" textLength="158" lengthAdjust="spacingAndGlyphs">Offices: Brookvale, FL</text>
      <g class="bulb--off">
        <path d="M37 165a12 12 0 0 0-8 21v6h16v-6a12 12 0 0 0-8-21z"/>
        <rect x="30" y="194" width="14" height="3"/>
        <rect x="32" y="198" width="10" height="3"/>
      </g>
      <text class="cta" x="149" y="325" text-anchor="middle" font-size="171" textLength="263" lengthAdjust="spacingAndGlyphs">CONTACT</text>
      <text class="cta" x="148" y="384" text-anchor="middle" font-size="79" textLength="256" lengthAdjust="spacingAndGlyphs">THE COUNSEL DESK</text>
      <text class="phone" x="149" y="429" text-anchor="middle" textLength="198" lengthAdjust="spacingAndGlyphs">1-855-ROW-4738</text>
      <text class="web" x="148" y="452" text-anchor="middle" textLength="196" lengthAdjust="spacingAndGlyphs">www.TheCounselDesk.com</text>
    </svg>
  </article>

  <article class="banner banner--lit">
    <div class="runway-photo" role="img" aria-label="Yellow-tinted photo of a jet airliner nose-on at a night runway"></div>
    <svg class="artwork" viewBox="0 0 300 600">
      <circle class="brand-dot" cx="42" cy="32" r="17"/>
      <text class="brand-name" x="177" y="32" text-anchor="middle" textLength="152" lengthAdjust="spacingAndGlyphs">The Marlow Law Firm</text>
      <line class="practice-rule" x1="88" y1="43" x2="116" y2="43"/>
      <text class="practice" x="186" y="46" text-anchor="middle" textLength="136" lengthAdjust="spacingAndGlyphs">AVIATION LAW | DRONE LAW</text>
      <line class="practice-rule" x1="257" y1="43" x2="272" y2="43"/>
      <rect class="tagline-band" x="0" y="73" width="300" height="68"/>
      <text class="tagline" x="152" y="105" text-anchor="middle" textLength="146" lengthAdjust="spacingAndGlyphs">VECTORING YOU</text>
      <text class="tagline" x="152" y="129" text-anchor="middle" textLength="272" lengthAdjust="spacingAndGlyphs">THROUGH LEGAL TURBULENCE</text>
      <text class="office" x="150" y="168" text-anchor="middle" textLength="158" lengthAdjust="spacingAndGlyphs">Offices: Brookvale, FL</text>
      <g class="bulb-rays">
        <line x1="37" y1="155" x2="37" y2="160"/>
        <line x1="24" y1="158" x2="27" y2="163"/>
        <line x1="50" y1="158" x2="47" y2="163"/>
        <line x1="13" y1="167" x2="19" y2="169"/>
        <line x1="61" y1="167" x2="55" y2="169"/>
        <line x1="13" y1="177" x2="19" y2="176"/>
        <line x1="61" y1="177" x2="55" y2="176"/>
      </g>
      <g class="bulb--on">
        <path d="M37 165a12 12 0 0 0-8 21v6h16v-6a12 12 0 0 0-8-21z"/>
        <rect x="30" y="194" width="14" height="3"/>
        <rect x="32" y="198" width="10" height="3"/>
      </g>
      <path d="M34 190v-9l3 3 3-3v9" fill="none" stroke="#000" stroke-width="1.2"/>
      <text class="cta" x="149" y="325" text-anchor="middle" font-size="171" textLength="263" lengthAdjust="spacingAndGlyphs">CONTACT</text>
      <text class="cta" x="148" y="384" text-anchor="middle" font-size="79" textLength="256" lengthAdjust="spacingAndGlyphs">THE COUNSEL DESK</text>
      <rect class="divider" x="82" y="398" width="134" height="3"/>
      <text class="phone" x="149" y="429" text-anchor="middle" textLength="198" lengthAdjust="spacingAndGlyphs">1-855-ROW-4738</text>
      <text class="web" x="148" y="452" text-anchor="middle" textLength="196" lengthAdjust="spacingAndGlyphs">www.TheCounselDesk.com</text>
    </svg>
  </article>

</main>
</body>
</html>
```